Electrician's Business needs web site for customers to get professional impression of business.

Have a logo, need a web page for customers to visit. Web page should make it easy for customers to approach /contact me, if possible a way for customers to leave their details so I can call them back.
A description/ list of services and advertise how my service is different and better than other electricians.
A gallery to upload photos to, to show completed works from past projects.
Updates

Target Market(s)

Domestic/residential home owner/renter/builder

Industry/Entity Type

Electrician

Coding

Coded - Design and coding required

Number of Pages Required

2 page

Font styles to use
Sans Serif

Colors
0255a3
ffffff

Requirements
Must have
• Appeal to home owner/renter, domestic market.
• Capture contact details of customer & advertise my contact details.
• List of services
Nice to have
• A photo gallery, so I can upload pictures of completed work.
Should not have
• Industrial/construction images.

```html
<!DOCTYPE html>
<html lang="en">
<head>
<meta charset="utf-8">
<title>Volt Mate – Electrical Services</title>
<link href="https://fonts.googleapis.com/css2?family=Titillium+Web:wght@400;600;700&display=swap" rel="stylesheet">
<style>
:root{
  --blue:#0e4d96;
  --blue-dark:#0a3f80;
  --orange:#f28a2e;
  --white:#ffffff;
  --grey-band:#f3f3f3;
  --text:#555a60;
  --line:#cfd3d8;
}
*{box-sizing:border-box;margin:0;padding:0}
html,body{width:1200px;height:3243px;overflow:hidden}
body{position:relative;background:var(--white);font-family:"Titillium Web",sans-serif;color:var(--text)}
.abs{position:absolute}
.shapes{position:absolute;left:0;top:0;width:1200px;height:3243px}

/* header */
.brand{position:absolute;display:flex;align-items:center;gap:8px;color:var(--white);font-weight:700;font-size:30px;line-height:1}
.brand-dot{width:14px;height:14px;border-radius:50%;background:var(--orange)}
.main-nav{left:537px;top:50px;display:flex;gap:29px}
.main-nav a{color:var(--white);text-decoration:none;font-size:16px;position:relative;padding-bottom:8px}
.main-nav a.active::after{content:"";position:absolute;left:0;right:0;bottom:0;height:3px;background:var(--orange)}

/* hero */
.hero{left:162px;top:115px;width:874px;height:339px;overflow:hidden}
.hero-photo{position:absolute;right:0;top:0;width:500px;height:339px;background:linear-gradient(120deg,#9fa7ae,#6f7d8a 50%,#3b4d66)}
.hero-panel{position:absolute;left:0;top:0;width:874px;height:339px}
.hero-title{left:37px;top:115px;color:var(--white);font-weight:600;font-size:40px;line-height:1.1}
.hero-sub{left:37px;top:160px;color:var(--white);font-size:20px}
.btn{display:inline-flex;align-items:center;justify-content:center;color:var(--white);text-decoration:none;font-weight:600}
.btn-blue{background:var(--blue)}
.btn-orange{background:var(--orange)}
.hero-btn{left:37px;top:209px;width:121px;height:35px;font-size:12px;font-weight:400}
.dots{left:32px;top:305px;display:flex;gap:6px}
.dots span{width:9px;height:9px;border-radius:50%;background:var(--white)}
.dots span.on{background:#222}

.welcome-title{left:0;width:1200px;top:515px;text-align:center;color:var(--orange);font-weight:700;font-size:37px}
.welcome-text{left:173px;width:856px;top:595px;text-align:center;color:var(--white);font-size:13px;line-height:22px}

.section-title{left:0;width:1200px;text-align:center;font-weight:700;font-size:37px}
.orange{color:var(--orange)}
.blue{color:var(--blue)}

/* services */
.service-photo{top:953px;width:425px;height:264px}
.photo-commercial{left:162px;background:linear-gradient(180deg,#5d7188,#3c4c5f 55%,#2b343d)}
.photo-residential{left:612px;background:linear-gradient(180deg,#3f7fd0,#8fb4de 45%,#4d5a4a 75%,#6e7f4d)}
.service-name{top:1255px;color:var(--orange);font-weight:700;font-size:19px}
.service-text{top:1298px;width:425px;font-size:14px;line-height:22px}
.service-btn{top:1418px;width:115px;height:35px;font-size:13px}

/* gallery */
.gallery{left:162px;top:1747px;width:874px;height:398px;display:grid;grid-template-columns:291px 292px 291px;grid-template-rows:199px 199px}
.tile:nth-child(1){background:linear-gradient(135deg,#4a4038,#2d2925)}
.tile:nth-child(2){background:linear-gradient(180deg,#e6a25d,#c46a4a 55%,#3a2b3b)}
.tile:nth-child(3){background:linear-gradient(135deg,#c9ccd1,#7f8a99 60%,#3d4d6a)}
.tile:nth-child(4){background:linear-gradient(135deg,#e5dccd,#c4b79f 50%,#4d6ea8)}
.tile:nth-child(5){background:linear-gradient(135deg,#d9a07a,#5d8dc8 60%,#2e3d55)}
.tile:nth-child(6){background:linear-gradient(135deg,#d8d2c4,#6c7887 55%,#2d3b52)}
.tile-feature{position:relative;display:flex;flex-direction:column;align-items:center;justify-content:center;text-align:center;color:var(--white)}
.tile-feature h3{font-size:20px;font-weight:700;margin-top:8px}
.tile-feature p{font-size:11px;line-height:16px;width:230px;margin:6px 0 10px}
.tile-feature .btn{width:90px;height:24px;font-size:10px}
.gallery-btn{left:515px;top:2192px;width:170px;height:50px;font-size:15px}

/* contact */
.address{left:173px;top:2550px;width:200px}
.address h4{color:var(--orange);font-size:18px;font-weight:700;margin-bottom:8px}
.address p{font-size:11px;line-height:19px;color:#444}
.address p+p{margin-top:16px}
.field{border:1px solid var(--line);background:var(--white);font-size:11px;color:#444;padding:6px 7px}
.send-btn{left:393px;top:2720px;width:102px;height:32px;font-size:11px}

/* footer */
.footer-brand{left:0;width:1200px;top:3022px;justify-content:center}
.footer-nav{left:0;width:1200px;top:3093px;display:flex;justify-content:center;gap:32px}
.footer-nav a{color:var(--white);text-decoration:none;font-size:16px}
.copyright{left:0;width:1200px;top:3138px;text-align:center;color:var(--white);font-size:15px}
</style>
</head>
<body>

<svg class="shapes" viewBox="0 0 1200 3243" aria-hidden="true">
  <rect x="0" y="0" width="1200" height="789" fill="var(--blue)"/>
  <polygon points="0,1611 573,1500 573,1555 1200,1475 1200,2230 660,2345 660,2280 0,2400" fill="var(--grey-band)"/>
  <polygon points="0,2940 562,2832 562,2940 1200,2804 1200,3243 0,3243" fill="var(--blue)"/>
</svg>

<div class="brand" style="left:169px;top:44px"><span>Volt Mate</span><span class="brand-dot"></span></div>
<nav class="abs main-nav">
  <a href="#" class="active">Home</a>
  <a href="#">About Us</a>
  <a href="#">Services</a>
  <a href="#">Projects</a>
  <a href="#">Clients</a>
  <a href="#">Contact Us</a>
</nav>

<section class="abs hero">
  <div class="hero-photo" role="img" aria-label="Electrician in a hard hat wiring a distribution panel"></div>
  <svg class="hero-panel" viewBox="0 0 874 339" aria-hidden="true">
    <polygon points="0,0 420,0 380,339 0,339" fill="var(--orange)"/>
  </svg>
  <div class="abs hero-title">Volt Mate</div>
  <div class="abs hero-sub">Eletrician Service</div>
  <a href="#" class="abs btn btn-blue hero-btn">LEARN MORE</a>
  <div class="abs dots"><span class="on"></span><span></span><span></span><span></span></div>
</section>

<h1 class="abs welcome-title">Welcome to Volt Mate</h1>
<p class="abs welcome-text">Sed ut perspiciatis unde omnis iste natus error sit voluptatem accusantium doloremque laudantium, totam rem aperiam, eaque ipsa quae ab illo inventore veritatis et quasi architecto beatae vitae dicta sunt explicabo. Nemo enim ipsam voluptatem quia voluptas sit aspernatur aut odit aut fugit, sed quia consequuntur magni dolores eos qui ratione voluptatem</p>

<h2 class="abs section-title orange" style="top:855px">Our Services</h2>

<div class="abs service-photo photo-commercial" role="img" aria-label="Modern glass office building at dusk"></div>
<div class="abs service-photo photo-residential" role="img" aria-label="Contemporary two-storey family home with lawn"></div>

<h3 class="abs service-name" style="left:162px">Commercial</h3>
<p class="abs service-text" style="left:162px">Sed ut perspiciatis unde omnis iste natus error sit voluptatem accusantium doloremque laudantium, totam rem aperiam, eaque ipsa quae ab illo inventore veritatis et quasi architecto beatae vitae dicta sunt explicabo. Nemo enim ipsam voluptatem</p>
<a href="#" class="abs btn btn-orange service-btn" style="left:162px">Read More</a>

<h3 class="abs service-name" style="left:612px">Residential</h3>
<p class="abs service-text" style="left:612px">Sed ut perspiciatis unde omnis iste natus error sit voluptatem accusantium doloremque laudantium, totam rem aperiam, eaque ipsa quae ab illo inventore veritatis et quasi architecto beatae vitae dicta sunt explicabo. Nemo enim ipsam voluptatem</p>
<a href="#" class="abs btn btn-orange service-btn" style="left:612px">Read More</a>

<h2 class="abs section-title blue" style="top:1658px">Photo Gallery</h2>

<div class="abs gallery">
  <div class="tile tile-feature" role="img" aria-label="Electrician at work, darkened behind a caption">
    <h3>Volt Mate</h3>
    <p>Sed ut perspiciatis unde omnis iste natus error sit voluptatem accusantium doloremque</p>
    <span class="btn btn-blue">VIEW DETAILS</span>
  </div>
  <div class="tile" role="img" aria-label="Line workers on a pylon at sunset"></div>
  <div class="tile" role="img" aria-label="Electrician testing a breaker board"></div>
  <div class="tile" role="img" aria-label="Electrician in a white helmet holding a meter"></div>
  <div class="tile" role="img" aria-label="Smiling electrician beside a wired fuse box"></div>
  <div class="tile" role="img" aria-label="Electrician in a yellow hard hat fitting a panel"></div>
</div>

<a href="#" class="abs btn btn-blue gallery-btn">VIEW GALLERY</a>

<h2 class="abs section-title orange" style="top:2432px">Contact Us</h2>

<div class="abs address">
  <h4>Address</h4>
  <p>3rd Floor, Block B,<br>Harbour Works Bldg.,<br>27 Lantern Road, Kowloon,<br>Hong Kong</p>
  <p>PHONE &nbsp;(+852) 3100 4820 /<br>FAX &nbsp;&nbsp;(+852) 3100 4821</p>
  <p>EMAIL &nbsp;&nbsp;&nbsp;&nbsp;&nbsp;&nbsp;hello@voltmate.example<br>WEBSITE &nbsp;&nbsp;http://www.voltmate.example</p>
</div>

<div class="abs field" style="left:393px;top:2562px;width:271px;height:33px">Name</div>
<div class="abs field" style="left:393px;top:2614px;width:271px;height:33px">E-mail</div>
<div class="abs field" style="left:393px;top:2666px;width:271px;height:33px">Phone</div>
<div class="abs field" style="left:681px;top:2562px;width:272px;height:140px">Message</div>
<a href="#" class="abs btn btn-blue send-btn">SEND</a>

<div class="brand footer-brand"><span>Volt Mate</span><span class="brand-dot"></span></div>
<nav class="abs footer-nav">
  <a href="#">Home</a>
  <a href="#">About Us</a>
  <a href="#">Services</a>
  <a href="#">Projects</a>
  <a href="#">Clients</a>
  <a href="#">Contact Us</a>
</nav>
<p class="abs copyright">© 2016 Company Name | &nbsp;All Rights Reserved</p>

</body>
</html>
```